Business Card Design Project

A polished, very professional looking business card. I think we want to keep it all grey. I've attached our old logo, and current mockup in which case we really like the font.

Target Market(s)

Target Market are Bride and Grooms and Wedding Coordinators. We are wedding photographers

Industry/Entity Type

Business

Font styles to use
Serif
Sans Serif

Requirements
Must have
• An elegant, yet simple and sophisticated appearance.

Phone number, Email, Website and Social Media link.
Nice to have
• An element that can be spot glossed when printed. Not necessary though.
Should not have
• Bright colors, images or intensive graphics.

```html
<!DOCTYPE html>
<html lang="en">
<head>
<meta charset="utf-8">
<title>Dalton Merrow Photographers — Business Cards</title>
<link href="https://fonts.googleapis.com/css2?family=Cinzel:wght@400&family=Montserrat:wght@300;400&display=swap" rel="stylesheet">
<style>
  :root {
    --backdrop: #e6e6e4;
    --card: #f4f4f3;
    --shade: #d9d9d8;
    --rule: #c4c4c3;
    --ink: #3b3b3c;
    --ink-soft: #6e6e70;
  }
  * { box-sizing: border-box; margin: 0; padding: 0; }
  html, body {
    width: 1200px; height: 1000px; overflow: hidden;
    background: var(--backdrop);
  }
  .sheet {
    width: 1200px; height: 1000px;
    display: flex; align-items: center; justify-content: center; gap: 40px;
  }
  .card {
    position: relative;
    width: 540px; height: 309px;
    background: var(--card);
    box-shadow: 0 2px 10px rgba(0,0,0,0.12);
    overflow: hidden;
  }
  .card .rules { position: absolute; inset: 0; }

  /* back: contact details */
  .contact-list {
    position: absolute; left: 190px; top: 78px;
    list-style: none;
    font-family: "Montserrat", sans-serif; font-weight: 400;
    font-size: 15px; color: var(--ink);
    display: flex; flex-direction: column; align-items: flex-start; gap: 6px;
  }
  .contact-list .divider {
    width: 26px; height: 1px; background: var(--ink-soft); margin: 4px 0 4px 8px;
  }

  /* front: identity */
  .shade-band {
    position: absolute; left: 0; top: 0; width: 100%; height: 118px;
    background: linear-gradient(180deg, var(--shade), #e4e4e3);
  }
  .identity {
    position: absolute; left: 0; right: 0; top: 78px;
    display: flex; flex-direction: column; align-items: center;
  }
  .identity .mark {
    width: 34px; height: 34px; background: var(--ink);
  }
  .identity .mark-rule {
    width: 28px; height: 1px; background: var(--ink-soft); margin: 10px 0 12px;
  }
  .identity .name {
    font-family: "Cinzel", serif; font-weight: 400;
    font-size: 24px; letter-spacing: 0.32em; color: var(--ink);
    padding-left: 0.32em;
  }
  .identity .trade {
    margin-top: 8px;
    font-family: "Montserrat", sans-serif; font-weight: 300;
    font-size: 9px; letter-spacing: 0.55em; color: var(--ink-soft);
    padding-left: 0.55em;
  }
</style>
</head>
<body>
<main class="sheet">

  <section class="card card-back" aria-label="Card back with contact details">
    <svg class="rules" width="540" height="309" viewBox="0 0 540 309" aria-hidden="true">
      <g stroke="var(--rule)" stroke-width="2">
        <line x1="60" y1="14" x2="60" y2="120"/>
        <line x1="110" y1="0" x2="110" y2="58"/>
        <line x1="478" y1="230" x2="478" y2="309"/>
      </g>
    </svg>
    <ul class="contact-list">
      <li>phone number</li>
      <li class="divider" aria-hidden="true"></li>
      <li>email</li>
      <li class="divider" aria-hidden="true"></li>
      <li>website</li>
      <li class="divider" aria-hidden="true"></li>
      <li>social media link</li>
    </ul>
  </section>

  <section class="card card-front" aria-label="Card front with studio name">
    <div class="shade-band"></div>
    <svg class="rules" width="540" height="309" viewBox="0 0 540 309" aria-hidden="true">
      <g stroke="var(--rule)" stroke-width="2">
        <line x1="440" y1="200" x2="440" y2="300"/>
        <line x1="484" y1="220" x2="484" y2="309"/>
        <line x1="510" y1="150" x2="510" y2="309"/>
      </g>
    </svg>
    <div class="identity">
      <div class="mark" aria-hidden="true"></div>
      <div class="mark-rule" aria-hidden="true"></div>
      <h1 class="name">DALTON MERROW</h1>
      <p class="trade">PHOTOGRAPHERS</p>
    </div>
  </section>

</main>
</body>
</html>
```